Flyer-Design für Vegane und Gluten freie Haarpflege
Zielgruppe
Herstellung + Vertrieb von VEGANEN Haarpflegeprodukten
Shampoo, Conditioner Gluten frei und Vegan nicht an Tieren getestet und biologisch abbaubar
Aufgabenstellung
DIN 4 Grösse 2 Seiten Produktinformation für Verbraucher

```html
<!DOCTYPE html>
<html lang="de">
<head>
<meta charset="utf-8">
<title>Verde Pura – Produktinformation</title>
<link href="https://fonts.googleapis.com/css2?family=Montserrat:wght@300;400;500;700&display=swap" rel="stylesheet">
<style>
  :root {
    --bg: #a9a8ad;
    --paper: #f1f1f1;
    --paper-soft: #e9e9ea;
    --panel: #7a7a7b;
    --panel-text: #f4f4f4;
    --ink: #2b2b2b;
    --ink-soft: #555;
    --heading-light: #d9d9d9;
    --leaf: #8dbb2b;
    --photo-blonde-a: #8d8d9e;
    --photo-blonde-b: #e6d7bd;
    --photo-yellow: #eeb22a;
    --photo-bottles: #d6d6d8;
  }
  * { margin: 0; padding: 0; box-sizing: border-box; }
  html, body { width: 1200px; height: 1050px; overflow: hidden; }
  body {
    background: var(--bg);
    font-family: "Montserrat", sans-serif;
    color: var(--ink);
    position: relative;
  }
  .page {
    position: absolute;
    top: 275px;
    width: 360px;
    height: 500px;
    background: var(--paper);
    box-shadow: 0 6px 18px rgba(0,0,0,.18);
    overflow: hidden;
  }
  .inside-left { left: 40px; }
  .inside-right { left: 400px; }
  .cover { left: 800px; background: var(--paper-soft); }

  .body-text { font-size: 7px; line-height: 1.45; text-align: justify; }
  .body-text p + p { margin-top: 6px; }
  .body-text strong { font-weight: 700; }

  /* inside left */
  .spread-heading {
    position: absolute; left: 22px; top: 24px; right: 22px;
    font-size: 13px; font-weight: 400; letter-spacing: .06em; line-height: 1.25;
    text-transform: uppercase; color: var(--ink);
  }
  .inside-left .col-a { position: absolute; left: 22px; top: 80px; width: 150px; color: var(--ink-soft); }
  .inside-left .col-b { position: absolute; left: 188px; top: 80px; width: 150px; color: var(--ink-soft); }
  .product-row {
    position: absolute; left: 22px; bottom: 22px; width: 316px; height: 150px;
    background: linear-gradient(180deg, var(--photo-bottles), #f5f5f5);
  }

  /* inside right */
  .inside-right .panel {
    position: absolute; left: 0; top: 26px; width: 334px; height: 448px;
    background: var(--panel); color: var(--panel-text);
  }
  .panel-heading {
    position: absolute; left: 14px; top: 12px; width: 150px;
    font-size: 12px; font-weight: 300; letter-spacing: .06em; line-height: 1.2;
    text-transform: uppercase; color: var(--heading-light);
  }
  .photo-hair {
    position: absolute; right: 0; top: 0; width: 168px; height: 178px;
    background: linear-gradient(135deg, var(--photo-blonde-a), var(--photo-blonde-b) 60%, #c99f7f);
  }
  .inside-right .col-a { position: absolute; left: 14px; top: 82px; width: 145px; }
  .inside-right .col-b { position: absolute; left: 176px; top: 190px; width: 146px; }
  .photo-curls {
    position: absolute; left: 0; bottom: 0; width: 160px; height: 118px;
    background: linear-gradient(160deg, var(--photo-yellow), #e0a020);
  }

  /* cover */
  .brand-square {
    position: absolute; left: 90px; top: 0; width: 230px; height: 230px;
    background: var(--panel);
    display: flex; align-items: center; justify-content: center; gap: 8px;
  }
  .brand-mark { width: 10px; height: 10px; background: var(--panel-text); border-radius: 50%; }
  .brand-name {
    color: var(--panel-text); font-size: 13px; font-weight: 400;
    letter-spacing: .12em; text-transform: uppercase;
  }
  .cover-rule { position: absolute; left: 40px; width: 280px; height: 1px; background: var(--ink); }
  .rule-top { top: 262px; }
  .rule-bottom { top: 346px; }
  .cover-title {
    position: absolute; left: 40px; top: 272px; width: 280px; text-align: center;
    font-size: 30px; font-weight: 500; letter-spacing: .04em; color: #1e1e1e;
  }
  .cover-sub {
    position: absolute; left: 40px; top: 313px; width: 280px; text-align: center;
    font-size: 9px; font-weight: 400; letter-spacing: .06em; line-height: 1.35;
    text-transform: uppercase; color: var(--ink-soft);
  }
  .vegan-claim {
    position: absolute; left: 40px; top: 364px; width: 280px;
    display: flex; align-items: center; justify-content: center; gap: 8px;
  }
  .vegan-shape { display: block; }
  .vegan-text { font-size: 12px; font-weight: 400; color: var(--ink); letter-spacing: .02em; }
  .vegan-text strong { font-weight: 700; }
  .cover-note {
    position: absolute; left: 40px; top: 420px; width: 280px; text-align: center;
    font-size: 8px; line-height: 1.4; color: var(--ink-soft);
  }
</style>
</head>
<body>

<section class="page inside-left">
  <h2 class="spread-heading">Verde Pura mit edlen Rohstoffen<br>aus nachhaltigen Ressourcen</h2>
  <div class="body-text col-a">
    <p>Es ist ganz einfach, um Säure auszugleichen braucht man Base, um Base zu neutralisieren benötigt man Säure. Daher muss man vor und nach dem Haare waschen immer einen pH-Ausgleich machen. Der Balancer ist ein Muss vor und nach jeglicher Haarwäsche, um die Kopfhaut zu neutralisieren. Shampoos müssen entweder etwas saurer oder basischer eingestellt sein, somit kann die Kopfhaut schon während der Reinigung auf den neutralen pH-Wert zurückgeführt werden.</p>
    <p><strong>VERDE PURA Balancer</strong> ist Gluten frei und Vegan, nicht an Tieren getestet und biologisch abbaubar.</p>
  </div>
  <div class="body-text col-b">
    <p>Es ist ganz einfach, um Säure auszugleichen braucht man Base, um Base zu neutralisieren benötigt man Säure. Daher muss man vor und nach dem Haare waschen immer einen pH-Ausgleich machen. Der Balancer ist ein Muss vor und nach jeglicher Haarwäsche, um die Kopfhaut zu neutralisieren. Shampoos müssen entweder etwas saurer oder basischer eingestellt sein, somit kann die Kopfhaut schon während der Reinigung auf den neutralen pH-Wert zurückgeführt werden.</p>
    <p><strong>VERDE PURA Balancer</strong> ist Gluten frei und Vegan, nicht an Tieren getestet und biologisch abbaubar.</p>
  </div>
  <div class="product-row" role="img" aria-label="Produktfoto: fünf weiße Shampooflaschen mit grauem Etikett in einer Reihe"></div>
</section>

<section class="page inside-right">
  <div class="panel">
    <h2 class="panel-heading">Verde Pura hat das passende Shampoo zu Ihrem Haartyp</h2>
    <div class="photo-hair" role="img" aria-label="Foto: Frau mit langem, wehendem blondem Haar"></div>
    <div class="body-text col-a">
      <p>Bei Afrikanischen, Asiatischen &amp; Mediterranen Typen ist die Sonnenstrahlung intensiver, die Haut wird dunkler. Sie produziert nun viel mehr Farbpigmente um die Haut vor der starken Sonneneinstrahlung zu schützen. Durch Sonne und Wärme transpiriert der Körper. Salze und Feuchtigkeit werden dem Körper entzogen. Daher neigen Menschen im Süden mehr zu trockener Haut, Kopfhaut und Haaren. Die Pflege der Haare sollte mehr feuchtigkeitsspendend sein.</p>
      <p><strong>VERDE PURA Shampoo sicca fina</strong> ist Gluten frei und Vegan, nicht an Tieren getestet und biologisch abbaubar.</p>
    </div>
    <div class="body-text col-b">
      <p>Die Keltischen, Nordischen &amp; Mittel-europäischen Typen haben eine höhere Fettproduktion um sich vor Kälte zu schützen. Genetisch bedingt findet man diese Haartypen eher in östlichen und nördlichen Regionen. Im Norden ist es kälter als am Äquator, weil der Einstrahlwinkel der Sonnenstrahlen kleiner und damit die Fläche, die von einem bestimmten Sonnenstrahlbündel beschienen wird, größer ist.</p>
      <p><strong>VERDE PURA Shampoo lumen fina</strong> ist Gluten frei und Vegan, nicht an Tieren getestet und biologisch abbaubar.</p>
    </div>
    <div class="photo-curls" role="img" aria-label="Foto: lächelnde Frau mit Lockenkopf und Brille vor gelbem Hintergrund"></div>
  </div>
</section>

<section class="page cover">
  <div class="brand-square">
    <span class="brand-mark"></span>
    <span class="brand-name">Lena Marquardt</span>
  </div>
  <div class="cover-rule rule-top"></div>
  <h1 class="cover-title">VERDE PURA</h1>
  <p class="cover-sub">Mit edlen Rohstoffen<br>aus nachhaltigen Ressourcen</p>
  <div class="cover-rule rule-bottom"></div>
  <div class="vegan-claim">
    <svg class="vegan-shape" width="40" height="28" viewBox="0 0 40 28" aria-hidden="true">
      <ellipse cx="20" cy="14" rx="19" ry="12" fill="var(--leaf)"/>
    </svg>
    <span class="vegan-text">100% <strong>Vegan</strong></span>
  </div>
  <p class="cover-note">ohne Tierversuche<br>und biologisch abbaubar</p>
</section>

</body>
</html>
```